Banner signature

Hi, looking for a banner for email signature 728 px wide and 200 px high
Could we have our 10 year logo and premium logo, a similar look and feel of our previous banner design (I've attached) and also include an aboriginal design with the Wording
This email comes to you from Gubbi Gubbi country
I've attached an example of some look and feels that we like.
Can we have the background of banner the Blue colour of our Fern & Tide logo and

```html
<!DOCTYPE html>
<html lang="en">
<head>
<meta charset="utf-8">
<title>Email Signature Banner – Fern &amp; Tide</title>
<link rel="stylesheet" href="https://fonts.googleapis.com/css2?family=Gochi+Hand&family=Open+Sans:wght@700&display=swap">
<style>
  :root {
    --page: #ffffff;
    --sky-blue: #19aef0;
    --dot-white: #ffffff;
    --text-white: #ffffff;
    --ring-teal: #3cc3c3;
    --ring-red: #d9293a;
    --ring-maroon: #7a2232;
    --gold-light: #f6df8a;
    --gold-mid: #d9ad3c;
    --gold-deep: #a9781c;
    --name-ink: #1c2a39;
  }
  * { margin: 0; padding: 0; box-sizing: border-box; }
  html, body {
    width: 1200px;
    height: 467px;
    overflow: hidden;
    background: var(--page);
  }
  .canvas {
    position: relative;
    width: 1200px;
    height: 467px;
  }
  .banner {
    position: absolute;
    left: 67px;
    top: 88px;
    width: 1070px;
    height: 292px;
    background: var(--sky-blue);
    overflow: hidden;
    box-shadow: 0 4px 14px rgba(0, 0, 0, 0.18);
  }
  .banner__dots {
    position: absolute;
    left: 0;
    top: 0;
  }
  .heritage-ring {
    position: absolute;
    left: -5px;
    top: -43px;
    width: 344px;
    height: 344px;
    border-radius: 50%;
    background: radial-gradient(circle at 50% 50%,
      var(--gold-light) 0%, var(--gold-mid) 34%, var(--gold-deep) 38%,
      #ffffff 39%, #ffffff 44%, var(--ring-red) 45%, var(--ring-maroon) 56%,
      var(--ring-teal) 58%, var(--ring-teal) 100%);
  }
  .message {
    position: absolute;
    left: 345px;
    width: 420px;
    top: 0;
    height: 100%;
    text-align: center;
    color: var(--text-white);
  }
  .message__lead {
    position: absolute;
    top: 75px;
    width: 100%;
    font-family: "Open Sans", Arial, sans-serif;
    font-weight: 700;
    font-size: 13px;
    letter-spacing: 0.6px;
  }
  .message__country-name {
    position: absolute;
    top: 100px;
    width: 100%;
    font-family: "Gochi Hand", "Comic Sans MS", cursive;
    font-size: 68px;
    line-height: 1;
    letter-spacing: 1px;
  }
  .message__country-word {
    position: absolute;
    top: 196px;
    width: 100%;
    font-family: "Open Sans", Arial, sans-serif;
    font-weight: 700;
    font-size: 25px;
    letter-spacing: 0.5px;
  }
  .brand-panel {
    position: absolute;
    right: 0;
    top: 0;
  }
  .brand {
    position: absolute;
    left: 850px;
    width: 220px;
    top: 0;
    height: 100%;
  }
  .brand__seal {
    position: absolute;
    left: 50%;
    top: 36px;
    width: 150px;
    height: 150px;
    margin-left: -75px;
    border-radius: 50%;
    background: radial-gradient(circle at 38% 32%, var(--gold-light), var(--gold-mid) 55%, var(--gold-deep));
  }
  .brand__name {
    position: absolute;
    top: 212px;
    width: 100%;
    text-align: center;
    font-family: "Open Sans", Arial, sans-serif;
    font-weight: 700;
    font-size: 22px;
    color: var(--name-ink);
  }
</style>
</head>
<body>
  <main class="canvas">
    <section class="banner" aria-label="Email signature banner">
      <svg class="banner__dots" width="1070" height="292" aria-hidden="true">
        <line x1="330" y1="9" x2="790" y2="9" stroke="var(--dot-white)" stroke-width="3" stroke-linecap="round" stroke-dasharray="0 8"/>
        <line x1="330" y1="283" x2="790" y2="283" stroke="var(--dot-white)" stroke-width="3" stroke-linecap="round" stroke-dasharray="0 8"/>
      </svg>

      <div class="heritage-ring" role="img" aria-label="Aboriginal dot-art ring in teal, red and maroon framing the gold ten-year anniversary emblem"></div>

      <div class="message">
        <p class="message__lead">THIS EMAIL COMES TO YOU FROM</p>
        <p class="message__country-name">GUBBI GUBBI</p>
        <p class="message__country-word">COUNTRY</p>
      </div>

      <svg class="brand-panel" width="330" height="292" aria-hidden="true">
        <path d="M60 0 Q-10 146 60 292 L330 292 L330 0 Z" fill="var(--ring-red)"/>
        <path d="M68 0 Q0 146 68 292 L330 292 L330 0 Z" fill="var(--ring-teal)"/>
        <path d="M76 0 Q10 146 76 292 L330 292 L330 0 Z" fill="#ffffff"/>
      </svg>

      <div class="brand">
        <div class="brand__seal"></div>
        <p class="brand__name">Fern &amp; Tide</p>
      </div>
    </section>
  </main>
</body>
</html>
```